New Company Business Card design

Looking for a corporate looking business card utilising my new logo design - the logo i would like embossed as one option and flat as another - simplistic but stylish - less is more - we are an import export business launching into the market - i would like a couple of options as main background - Grey or Black

```html
<!DOCTYPE html>
<html lang="en">
<head>
<meta charset="utf-8">
<title>Corvant Trade Solutions – Business Card</title>
<link href="https://fonts.googleapis.com/css2?family=Crimson+Text:wght@400;600&display=swap" rel="stylesheet">
<style>
  :root {
    --page: #ffffff;
    --card: #333333;
    --gloss: #666666;
    --ink: #f2f2f2;
    --ink-soft: #bdbdbd;
    --brand-blue: #1a7fd0;
    --icon-grey: #777777;
  }
  html, body {
    margin: 0;
    padding: 0;
    width: 1200px;
    height: 1200px;
    overflow: hidden;
    background: var(--page);
    font-family: "Crimson Text", Georgia, serif;
  }
  .canvas { position: relative; width: 1200px; height: 1200px; }
  .card {
    position: absolute;
    left: 325px;
    width: 570px;
    height: 340px;
    background: var(--card);
    border-radius: 16px;
    overflow: hidden;
  }
  .card--front { top: 168px; }
  .card--back { top: 688px; }
  .gloss { position: absolute; left: 0; top: 0; width: 570px; height: 60px; }

  .brand {
    position: absolute;
    display: flex;
    align-items: center;
    gap: 12px;
    transform: translateX(-50%);
    white-space: nowrap;
  }
  .brand__mark {
    width: 40px; height: 40px;
    border-radius: 50%;
    background: var(--brand-blue);
    flex: none;
  }
  .brand__name {
    color: var(--brand-blue);
    font-weight: 600;
    font-size: 30px;
    line-height: 1.05;
    letter-spacing: 0.5px;
  }
  .card--front .brand { left: 170px; top: 132px; }
  .card--back .brand { left: 286px; top: 116px; }

  .holder {
    position: absolute;
    right: 32px;
    top: 72px;
    margin: 0;
    color: var(--ink);
    font-weight: 400;
    font-size: 26px;
  }
  .contact { position: absolute; inset: 0; margin: 0; padding: 0; list-style: none; }
  .contact__item {
    position: absolute;
    right: 32px;
    display: flex;
    align-items: center;
    gap: 14px;
    color: var(--ink);
    font-size: 19px;
    transform: translateY(-50%);
  }
  .contact__icon { width: 26px; height: 34px; display: block; }
  .contact__item--mobile { top: 150px; }
  .contact__item--phone { top: 200px; }
  .contact__item--web { top: 240px; right: 29px; }
  .contact__item--web .contact__text { margin-right: 16px; }
  .contact__item--mail { top: 284px; }

  .tagline {
    position: absolute;
    left: 0; right: 0;
    top: 272px;
    margin: 0;
    text-align: center;
    color: var(--ink-soft);
    font-size: 27px;
    font-weight: 400;
  }
</style>
</head>
<body>
<div class="canvas">

  <section class="card card--front" aria-label="Business card front">
    <svg class="gloss" viewBox="0 0 570 60" aria-hidden="true">
      <polygon points="75,56 379,1 543,0" fill="var(--gloss)"/>
    </svg>

    <div class="brand">
      <span class="brand__mark"></span>
      <span class="brand__name">Corvant Trade<br>Solutions</span>
    </div>

    <h1 class="holder">Mr. Kiran Vale, Director</h1>

    <ul class="contact">
      <li class="contact__item contact__item--mobile">
        <span class="contact__text">++ 555 210</span>
        <svg class="contact__icon" viewBox="0 0 26 42" aria-hidden="true">
          <rect x="2" y="1" width="22" height="40" rx="3" fill="var(--brand-blue)"/>
          <rect x="5" y="5" width="16" height="31" fill="var(--icon-grey)"/>
        </svg>
      </li>
      <li class="contact__item contact__item--phone">
        <span class="contact__text">++ 555 390</span>
        <svg class="contact__icon" viewBox="0 0 26 26" aria-hidden="true">
          <circle cx="13" cy="13" r="11.5" fill="none" stroke="var(--brand-blue)" stroke-width="2"/>
          <path d="M9 7c-1.5 1-2 2.5-1 5 1 2.6 3 5 5.5 6.5 1.8 1 3 .8 4-.5l-2.3-2.3-1.7 1c-1.5-.8-3-2.5-3.6-4l1.2-1.5L9 7z" fill="var(--brand-blue)"/>
        </svg>
      </li>
      <li class="contact__item contact__item--web">
        <span class="contact__text">corvanttrade.com</span>
        <svg class="contact__icon" viewBox="0 0 30 30" aria-hidden="true">
          <path d="M15 2 1 15h4v13h7v-8h6v8h7V15h4z" fill="var(--brand-blue)"/>
        </svg>
      </li>
      <li class="contact__item contact__item--mail">
        <span class="contact__text">hello@corvanttrade.com</span>
        <svg class="contact__icon" viewBox="0 0 26 20" aria-hidden="true">
          <rect x="1" y="2" width="24" height="16" fill="var(--brand-blue)"/>
          <path d="M1 2l12 9 12-9M1 18l9-8M25 18l-9-8" fill="none" stroke="var(--card)" stroke-width="1.4"/>
        </svg>
      </li>
    </ul>
  </section>

  <section class="card card--back" aria-label="Business card back">
    <svg class="gloss" viewBox="0 0 570 60" aria-hidden="true">
      <polygon points="53,56 352,0 516,0" fill="var(--gloss)"/>
    </svg>

    <div class="brand">
      <span class="brand__mark"></span>
      <span class="brand__name">Corvant Trade<br>Solutions</span>
    </div>

    <p class="tagline">Import Export Business Launching</p>
  </section>

</div>
</body>
</html>
```